Halvern Aviation Group - "Coming Soon" Main Company Webpage

Design a main webpage that can be posted while a fully functional website is constructed. The design should be created to convey a sense of luxury and exclusivity. The main page should contain only one photo as the background. The photo I believe to show "luxury" and "Exclusivity" is listed as "Global Luxury Photo". I have included two other photos as well to aid in providing a variety of presentations.
The "Member PQTR" logo should appear somewhere on the main page but be less prevalent than the main company logo. "Coming Soon" should also appear to convey that a website is being constructed.
Tabs for the website:
- Aircraft Management
- Aircraft Sales
- Pilot Services
- Charter
- Flight Training

```html
<!DOCTYPE html>
<html lang="en">
<head>
<meta charset="utf-8">
<title>Halvern Aviation Group – Coming Soon</title>
<link rel="stylesheet" href="https://fonts.googleapis.com/css2?family=Michroma&family=Montserrat:wght@500;600&family=Orbitron:wght@500;600&display=swap">
<style>
  :root {
    --sky-deep: #3aa8e6;
    --sky-mid: #9fd2f2;
    --sky-light: #d8eefb;
    --cloud: #eef7fd;
    --brand-blue: #0a5aa8;
    --button-blue: #0b5aa5;
    --ink: #101820;
    --ink-soft: #1f2a36;
    --field-bg: rgba(235, 246, 253, 0.7);
    --field-border: rgba(255, 255, 255, 0.9);
    --jet-tone: #d9d4cc;
  }
  * { box-sizing: border-box; margin: 0; padding: 0; }
  html, body { width: 1200px; height: 576px; overflow: hidden; }
  body { font-family: "Montserrat", sans-serif; color: var(--ink); }

  .page {
    position: relative;
    width: 1200px;
    height: 576px;
    overflow: hidden;
  }
  .backdrop {
    position: absolute; inset: 0;
    background:
      radial-gradient(ellipse 420px 260px at 60px 190px, var(--sky-deep), transparent 70%),
      radial-gradient(ellipse 500px 200px at 700px 80px, var(--cloud), transparent 70%),
      radial-gradient(ellipse 600px 160px at 500px 560px, var(--cloud), transparent 70%),
      linear-gradient(180deg, var(--sky-mid) 0%, var(--sky-light) 100%);
  }
  .jet-photo {
    position: absolute;
    left: 585px; top: 266px;
    width: 615px; height: 237px;
    background: radial-gradient(ellipse 55% 50% at 65% 55%, var(--jet-tone), rgba(217,212,204,0.35) 55%, transparent 80%);
  }

  .site-header {
    position: absolute; left: 131px; top: 19px;
    width: 940px; height: 58px;
  }
  .brand {
    position: absolute; left: 0; top: 0;
    display: flex; align-items: center; gap: 9px;
    color: var(--brand-blue);
    font-family: "Michroma", sans-serif;
  }
  .brand-dot {
    width: 14px; height: 14px; border-radius: 50%;
    background: var(--brand-blue);
  }
  .brand-name { line-height: 1.05; font-size: 24px; letter-spacing: 1px; }
  .brand-name small { display: block; font-size: 12.5px; letter-spacing: 1.6px; }

  .main-nav {
    position: absolute; right: 0; top: 28px;
    display: flex; gap: 12px;
    font-size: 12px; font-weight: 500; letter-spacing: 0.2px;
  }
  .main-nav a { color: var(--ink); text-decoration: none; }
  .main-nav .sep { color: #5a6b7a; }

  .launch {
    position: absolute; left: 0; top: 145px; width: 1200px;
    text-align: center;
  }
  .launch-title {
    font-family: "Michroma", sans-serif;
    font-size: 42px; font-weight: 400;
    color: var(--brand-blue);
    letter-spacing: 1px;
  }
  .countdown {
    margin-top: 26px;
    display: flex; justify-content: center; align-items: center; gap: 9px;
  }
  .count-box {
    height: 47px; width: 150px;
    border: 1px solid var(--brand-blue); border-radius: 3px;
    display: flex; align-items: baseline; justify-content: center; gap: 6px;
    padding-top: 11px;
  }
  .count-box.wide { width: 165px; }
  .count-num { font-family: "Orbitron", sans-serif; font-weight: 600; font-size: 22px; color: var(--ink); }
  .count-label { font-family: "Orbitron", sans-serif; font-weight: 500; font-size: 13px; color: #3b4652; letter-spacing: 0.5px; }
  .count-sep { color: var(--ink-soft); font-size: 14px; }

  .notify-text { margin-top: 20px; font-size: 15px; font-weight: 500; color: var(--ink-soft); }
  .subscribe-form { margin-top: 13px; display: flex; justify-content: center; gap: 18px; }
  .email-field {
    width: 263px; height: 41px;
    background: var(--field-bg); border: 1px solid var(--field-border); border-radius: 2px;
    padding: 0 16px; font: 500 12px "Montserrat", sans-serif; color: var(--ink);
  }
  .subscribe-btn {
    width: 112px; height: 41px;
    background: var(--button-blue); color: #fff; border: none; border-radius: 2px;
    font: 500 12px "Montserrat", sans-serif; letter-spacing: 0.3px;
  }

  .membership {
    position: absolute; left: 490px; top: 446px;
    display: flex; align-items: flex-end; gap: 14px;
  }
  .member-badge { width: 56px; height: 40px; border-radius: 50%; background: var(--brand-blue); }
  .member-text { display: flex; flex-direction: column; }
  .member-of { font-size: 13px; font-weight: 500; color: var(--ink); margin-left: 0; }
  .member-name { font-family: "Michroma", sans-serif; font-size: 30px; line-height: 1; color: var(--ink); letter-spacing: 2px; }
</style>
</head>
<body>
<div class="page">
  <div class="backdrop" role="img" aria-label="Bright blue sky with soft white clouds"></div>
  <div class="jet-photo" role="img" aria-label="Private business jet banking in flight"></div>

  <header class="site-header">
    <div class="brand">
      <span class="brand-dot"></span>
      <span class="brand-name">HALVERN<small>AVIATION GROUP</small></span>
    </div>
    <nav class="main-nav">
      <a href="#">AIRCRAFT MANAGEMENT</a><span class="sep">/</span>
      <a href="#">AIRCRAFT SALES</a><span class="sep">/</span>
      <a href="#">PILOT SERVICES</a><span class="sep">/</span>
      <a href="#">CHARTER</a><span class="sep">/</span>
      <a href="#">FLIGHT TRAINING</a>
    </nav>
  </header>

  <main class="launch">
    <h1 class="launch-title">COMING SOON</h1>
    <div class="countdown">
      <div class="count-box"><span class="count-num">23</span><span class="count-label">DAYS</span></div>
      <span class="count-sep">:</span>
      <div class="count-box"><span class="count-num">02</span><span class="count-label">HOURS</span></div>
      <span class="count-sep">:</span>
      <div class="count-box wide"><span class="count-num">33</span><span class="count-label">MINUTES</span></div>
    </div>
    <p class="notify-text">Get notified when site goes live:</p>
    <form class="subscribe-form">
      <input class="email-field" type="email" value="info@halvernmail.com" aria-label="Email address">
      <button class="subscribe-btn" type="button">SUBSCRIBE</button>
    </form>
  </main>

  <div class="membership">
    <span class="member-badge"></span>
    <div class="member-text">
      <span class="member-of">member of</span>
      <span class="member-name">PQTR</span>
    </div>
  </div>
</div>
</body>
</html>
```